納品ファイル PNG形式(.png)+ フォトショップ形式(.psd) お仕事の詳細: ▽バナー作成依頼の目的・概要 薬機法、景品表示法の観点から内容チェック(OK/NG判定)及び代替え提案までを即座にチェックできる 「広告表現チェックツール」のバナー制作をお任せします。 ※添付サービス資料になります。 ※複数採用させていただく場合もございます。 ※今回の依頼後、別案件を依頼させて頂く場合がございます。 ▽バナーのイメージ 信頼 ▽バナーの目的 販促 ▽テキスト ・必ず含めてほしいテキスト(全てご使用下さい) 広告表現における「薬機法」「景表法」を即時チェック +ロゴも必ず入れてください。 ・その他テキスト参考(ご使用に関してはお任せします。テキストの省略等も可) -薬機法、景品表示法の観点から広告表現チェック(OK/NG判定)及び代替え提案を実現 -リスティング広告の原稿や、SNS広告のテキスト原稿などのチェック! -今非常に問題になっている記事媒体のチェック! -画像における薬機法・景表法を画像上の文字解析機能を利用し、チェック! ▽画像素材 ロゴのみとなりますが、添付致します。 ▽デザイン案サイズ 300 × 250 ※提案は上記サイズのみで問題ありません。 ※当選連絡後にリサイズバナーサイズも納品してください。 ▽リサイズバナーサイズ =============== 120 × 60 468 × 60 234 × 60 250×250 100 × 60 320 × 50 =============== ▽注意点・禁止事項 ※他で登録されているデザインや商標の転用など、他社の知的財産権を侵すこと ※他のクライアントへ既に提案した内容の転用など ※作成いただいたバナーに関して、納品後はクライアントに帰属します。 たくさんの方からのご提案をお待ちしております。 |

```html
<!DOCTYPE html>
<html lang="ja">
<head>
<meta charset="utf-8">
<title>広告表現チェック バナー</title>
<link rel="stylesheet" href="https://fonts.googleapis.com/css2?family=Noto+Sans+JP:wght@500;700;900&display=swap">
<style>
  :root {
    --bg-deep: #0b0a1c;
    --bg-mid: #1c1738;
    --glow: #8a5cff;
    --glow-soft: rgba(150, 100, 255, 0.35);
    --white: #ffffff;
    --gold: #f6c21c;
    --gold-dark: #e2a300;
    --cyan: #3fd6ef;
    --ink: #111226;
    --footer: #141c3d;
    --footer-line: #2a3566;
  }
  html, body { margin: 0; padding: 0; overflow: hidden; }
  body {
    width: 1200px; height: 1000px;
    font-family: "Noto Sans JP", sans-serif;
    background: var(--bg-deep);
  }
  .banner {
    position: relative;
    width: 1200px; height: 1000px;
    overflow: hidden;
    background: radial-gradient(ellipse at 50% 40%, var(--bg-mid) 0%, var(--bg-deep) 75%);
  }
  .lead {
    position: absolute; top: 62px; left: 0; width: 100%;
    text-align: center; color: var(--white);
    font-size: 54px; font-weight: 700; letter-spacing: 2px; margin: 0;
  }
  .law-row {
    position: absolute; top: 192px; left: 78px;
    display: flex; align-items: center; gap: 24px;
  }
  .law-tag {
    display: inline-block; padding: 4px 34px 10px;
    transform: skewX(-12deg);
    font-size: 90px; font-weight: 900; color: var(--ink); line-height: 1.1;
  }
  .law-tag span { display: inline-block; transform: skewX(12deg); }
  .law-tag--yaku { background: var(--gold); }
  .law-tag--kei { background: var(--cyan); }
  .particle {
    color: var(--white); font-size: 62px; font-weight: 700; margin-left: 40px;
  }
  .visual {
    position: absolute; top: 320px; left: 0; width: 1200px; height: 320px;
    background:
      radial-gradient(circle at 86% 32%, #ffffff 0%, var(--glow) 6%, var(--glow-soft) 22%, transparent 45%),
      linear-gradient(100deg, rgba(214,170,140,0.55) 0%, rgba(214,170,140,0.35) 38%, transparent 72%);
  }
  .headline {
    position: absolute; top: 622px; left: 262px; margin: 0;
    font-size: 146px; font-weight: 900; color: var(--gold);
    transform: skewX(-10deg); letter-spacing: 2px;
    text-shadow: 0 4px 0 var(--gold-dark);
  }
  .footer {
    position: absolute; left: 0; bottom: 0; width: 100%; height: 168px;
    background: var(--footer); border-top: 2px solid var(--footer-line);
  }
  .brand {
    position: absolute; left: 50px; top: 56px;
    display: flex; align-items: center; gap: 20px;
    color: var(--white); font-size: 50px; font-weight: 500; letter-spacing: 6px;
  }
  .brand-mark { width: 44px; height: 44px; border-radius: 50%; background: var(--white); }
  .cta {
    position: absolute; right: 45px; top: 44px;
    width: 432px; height: 80px; border-radius: 40px;
    background: linear-gradient(180deg, #ffd64a 0%, var(--gold-dark) 100%);
    display: flex; align-items: center; justify-content: center; gap: 18px;
    color: var(--ink); font-size: 40px; font-weight: 700;
  }
</style>
</head>
<body>
  <div class="banner">
    <p class="lead">広告表現における</p>
    <div class="law-row">
      <div class="law-tag law-tag--yaku"><span>薬機法</span></div>
      <div class="law-tag law-tag--kei"><span>景表法</span></div>
      <span class="particle">を</span>
    </div>
    <div class="visual" role="img" aria-label="紫の稲妻の光に向かって指さす手の写真"></div>
    <h1 class="headline">即時チェック</h1>
    <div class="footer">
      <div class="brand"><span class="brand-mark"></span>CLEARAD</div>
      <div class="cta">詳しくはこちら
        <svg width="22" height="34" viewBox="0 0 22 34" aria-hidden="true"><path d="M4 3 L18 17 L4 31" fill="none" stroke="#111226" stroke-width="5" stroke-linecap="round" stroke-linejoin="round"/></svg>
      </div>
    </div>
  </div>
</body>
</html>
```